brikMOSA corporation pty ltd

Contruction industry
It's a wall and floor tiling business

Industry/Entity Type

Business

Requirements
Must have
• Likes-
- clean and easy to read
- a witty design is always well received
- for it to look reputable in the industry
- a strong and direct presentation
- simple but striking colour selection
Should not have
• Dislikes-
- pls no tacky square tiles to resemble tiling

```html
<!DOCTYPE html>
<html lang="en">
<head>
<meta charset="utf-8">
<title>brikmosa business card</title>
<link rel="stylesheet" href="https://fonts.googleapis.com/css2?family=Open+Sans:wght@300&display=swap">
<style>
  :root {
    --ink: #111111;
    --paper: #ffffff;
    --brand-green: #3f9c5b;
    --soft-green: #a4cfa4;
  }
  html, body {
    margin: 0;
    padding: 0;
    overflow: hidden;
    background: var(--paper);
  }
  .card {
    position: relative;
    width: 1200px;
    height: 798px;
    overflow: hidden;
    background: var(--paper);
    font-family: "Open Sans", Arial, sans-serif;
  }
  .card-art {
    position: absolute;
    inset: 0;
  }
  .wordmark {
    font-family: "Open Sans", Arial, sans-serif;
    font-weight: 300;
    font-size: 220px;
    letter-spacing: -4px;
    fill: var(--ink);
  }
  .contact-line {
    position: absolute;
    left: 128px;
    margin: 0;
    font-weight: 300;
    font-size: 76px;
    line-height: 1;
    letter-spacing: -2px;
    color: var(--ink);
    white-space: nowrap;
  }
  .contact-value { color: var(--brand-green); }
  .role-line   { top: 418px; }
  .mobile-line { top: 582px; }
  .email-line  { top: 653px; }
</style>
</head>
<body>
<main class="card">
  <svg class="card-art" width="1200" height="798" viewBox="0 0 1200 798">
    <defs>
      <clipPath id="sweep-clip">
        <path d="M0,0 L180,0 Q560,300 680,798 L0,798 Z"/>
      </clipPath>
    </defs>
    <path class="corner-sweep" d="M0,0 L180,0 Q560,300 680,798 L0,798 Z" fill="var(--soft-green)"/>
    <rect class="divider-bar" x="128" y="308" width="1052" height="56" fill="var(--soft-green)"/>
    <rect class="divider-bar-inset" x="128" y="308" width="1052" height="56" fill="var(--paper)" clip-path="url(#sweep-clip)"/>
    <text class="wordmark" x="122" y="272">brikmosa</text>
  </svg>

  <p class="contact-line role-line">director: <span class="contact-value">Ned Harlow</span></p>
  <p class="contact-line mobile-line">mobile: <span class="contact-value">0491 570 156</span></p>
  <p class="contact-line email-line">email: <span class="contact-value">ned.h@brikmosa.net</span></p>
</main>
</body>
</html>
```